Counselling practice needs a Business Card Design

I need a business card design for a new counselling practice in Canberra, Australia. The name of the practice is Dr Glen Hartwick, Counselling Services and the practice focuses on philosophical, narrative and existential counselling for individuals, couples and families. The final design should communicate professionalism, sophistication of analysis and psychological wholeness. The reverse side of the card should have an appointment reminder

Could the following qualifications also be included on card. BSc (Psychology), BA hons (Philosophy), PhD (Philosophy), Diploma of Community Counselling And the following affiliation Guild of Talk Therapists for the Southern Tablelands Inc. (GOTTST) And my contact phone mobile phone number is 0497385164, and email is drglenhartwick@quietharbourtherapy.example for inclusion as well.

Thank you all who have put in a design so far. I just wanted to clarify some design points based on what you have submitted. 1. The Guild of Talk Therapists. Southern Tablelands Inc. (GOTTST) is an affiliation only. 'Member of the Guild of Talk Therapists. Southern Tablelands Inc (GOTTST)' should appear with the same prominence of a qualification. 2. The Post Graduate Diploma in Community Counselling is a quaification and should appear as 'PG Dip (Community Counselling)' after the other qualifications. 3. I am advertising myself as a counsellor so 'Dr Glen Hartwick, Counselling Services' or 'Dr Glen Hartwick, Counsellor' is the equivalent of the business name. After looking at some of the designs I prefer Dr Glen Hartwick in sentence case rather than all capitals (DR GLEN HARTWICK). 4. 'Philosophical, narrative and existential counselling for individuals, couples and families' is the description of the type of counselling services and should appear on the card.

One further point. I have updated my email address for the card. It is now drglenhartwick@quietharbourtherapy.example

```html
<!DOCTYPE html>
<html lang="en">
<head>
<meta charset="utf-8">
<title>Dr Glen Hartwick – Counselling Services – Business Card</title>
<link href="https://fonts.googleapis.com/css2?family=Arimo:wght@400;700&display=swap" rel="stylesheet">
<style>
  :root {
    --bg: #e9e7e4;
    --card: #ffffff;
    --card-edge: #dcdcdc;
    --purple: #7b2fb3;
    --purple-light: #9047c9;
    --purple-dark: #6a239f;
    --rule: #c9b3dc;
    --band-text: #ffffff;
  }
  * { margin: 0; padding: 0; box-sizing: border-box; }
  html, body {
    width: 1200px; height: 858px; overflow: hidden;
    background: var(--bg);
    font-family: "Arimo", Arial, sans-serif;
  }
  .sheet {
    width: 1200px; height: 858px;
    display: flex; align-items: center; justify-content: center; gap: 50px;
  }
  .card {
    position: relative;
    width: 540px; height: 315px;
    background: var(--card);
    border: 1px solid var(--card-edge);
    box-shadow: 0 6px 18px rgba(0,0,0,0.12);
    overflow: hidden;
    color: var(--purple);
  }

  /* Front */
  .practice {
    position: absolute; left: 0; right: 0; top: 26px;
    text-align: center;
  }
  .practitioner-name { font-size: 27px; line-height: 1.1; letter-spacing: 0.3px; }
  .practice-title { font-size: 15px; line-height: 1.3; margin-top: 3px; }
  .services {
    font-size: 12.5px; line-height: 1.35; margin-top: 7px; opacity: 0.9;
  }
  .credentials {
    position: absolute; left: 0; right: 0; top: 128px;
    text-align: center;
  }
  .qualification { font-size: 13px; line-height: 1.5; opacity: 0.9; }
  .contact-band {
    position: absolute; left: 0; right: 0; bottom: 0; height: 64px;
    background: linear-gradient(90deg, var(--purple-dark), var(--purple-light) 45%, var(--purple));
    display: flex; align-items: center; justify-content: space-between;
    padding: 0 28px;
    color: var(--band-text);
    font-size: 14px;
  }
  .contact-item { display: flex; align-items: center; gap: 8px; white-space: nowrap; }
  .contact-icon { width: 14px; height: 14px; flex: none; }

  /* Back */
  .back {
    display: flex; flex-direction: column; align-items: center;
    padding-top: 40px;
    background: linear-gradient(180deg, #ffffff, #f2f2f2);
  }
  .reminder-title { font-size: 27px; line-height: 1.1; letter-spacing: 0.3px; }
  .reminder-note { font-size: 15px; line-height: 1.3; margin-top: 4px; }
  .reminder-fields {
    margin-top: 26px; width: 400px;
    display: flex; flex-direction: column; gap: 20px;
  }
  .field { display: flex; align-items: flex-end; gap: 10px; font-size: 15px; }
  .field-label { width: 52px; flex: none; }
  .field-line { flex: 1; border-bottom: 1px solid var(--rule); height: 16px; }
  .field-pair { display: flex; gap: 26px; }
  .field-pair .field { flex: 1; }
  .back-band {
    position: absolute; left: 0; right: 0; bottom: 0; height: 10px;
    background: linear-gradient(90deg, var(--purple-dark), var(--purple-light) 45%, var(--purple));
  }
</style>
</head>
<body>
<main class="sheet">
  <section class="card front">
    <div class="practice">
      <div class="practitioner-name">Dr Glen Hartwick</div>
      <div class="practice-title">Counselling Services</div>
      <div class="services">Philosophical, narrative and existential counselling<br>for individuals, couples and families</div>
    </div>
    <div class="credentials">
      <div class="qualification">BSc (Psychology) · BA hons (Philosophy) · PhD (Philosophy)</div>
      <div class="qualification">PG Dip (Community Counselling)</div>
      <div class="qualification">Member of the Guild of Talk Therapists. Southern Tablelands Inc (GOTTST)</div>
    </div>
    <div class="contact-band">
      <div class="contact-item">
        <svg class="contact-icon" viewBox="0 0 14 14" aria-hidden="true">
          <rect x="3" y="0.5" width="8" height="13" rx="1.5" fill="none" stroke="#fff" stroke-width="1.2"/>
          <rect x="4.5" y="2.5" width="5" height="5" fill="#fff"/>
          <circle cx="7" cy="11" r="0.9" fill="#fff"/>
        </svg>
        <span>0497385164</span>
      </div>
      <div class="contact-item">
        <svg class="contact-icon" viewBox="0 0 14 14" aria-hidden="true">
          <rect x="0.6" y="2.5" width="12.8" height="9" fill="none" stroke="#fff" stroke-width="1.2"/>
          <path d="M0.8 3 L7 8 L13.2 3" fill="none" stroke="#fff" stroke-width="1.2"/>
        </svg>
        <span>drglenhartwick@quietharbourtherapy.example</span>
      </div>
    </div>
  </section>

  <section class="card back">
    <div class="reminder-title">Appointment Reminder</div>
    <div class="reminder-note">Your next appointment with Dr Glen Hartwick</div>
    <div class="reminder-fields">
      <div class="field"><span class="field-label">Name</span><span class="field-line"></span></div>
      <div class="field-pair">
        <div class="field"><span class="field-label">Date</span><span class="field-line"></span></div>
        <div class="field"><span class="field-label">Time</span><span class="field-line"></span></div>
      </div>
    </div>
    <div class="back-band"></div>
  </section>
</main>
</body>
</html>
```